Open Horizon Circle - invitation / brochure

​​I am in need of a bi-fold invitation/brochure for an educational series called "Open Horizon Circle". This dinner series provides education and community for "Women in Transition" these are women who are currently getting divorced, recently divorced, or widowed.

I am a partner of a wealth management boutique that advises a small number of high-net-worth families. Additionally, I am married to one of the most prominent family law attorneys in the country. The combination of these two unique perspectives has allowed me to see there is an unfortunate dearth of impactful, powerful, and useful resources to help wealthy women transition from being married to being single. (via divorce and/or death of their spouse)

What, How & WHY I do my job:
As a wealth manager, the "what" and "how" aspects of my job are not materially different from most of my competitors. However, the thing that makes me completely unique, and without competition, is "why" I do my job.

I do this because so many women experience unwelcome and unproductive feelings when the dilution of their marriage is complete AND because there is virtually no good place for them to obtain the important information they truly need to move forward and lead a happy, full, prosperous, productive, and fun life. In the absence of this information, many women experience unwelcome, unpleasant, and unproductive emotions.

For example, some experience shame or fear that they have failed. Others struggle with the belief they wasted a significant portion of their life. Some struggle with unresolved anger over the entire experience. It's very difficult to process and work through these emotions by yourself and it can be hard to get the support and guidance they need from their best friends (most are not trained in this area) may well be married (functional or otherwise) and they often times don't have the times to be there when the newly divorced or widowed women need them most.

Usually, these negative feelings are most intense when they are looking backward in time. However, I have seen women go on and lead remarkably impressive lives. Lives that are ​more ​full, richer, more fun, dynamic, and rewarding than they expected possible.

More about the WHY I do what I do - I created Open Horizon Circle so women in transition have a safe, supportive and comfortable space for these women to support each other. While each woman's story is unique, the emotional consequences are fairly common and they do not need to feel alone as they process the sometimes difficult, conflicting, and unpredictable emotions.

I want them to connect with each other because they have a great appreciation and empathy for what all the other women are experiencing. A bi-product of attending and participating in the dinner is to forge friendships and connections with the other woman in attendance so they can be resources to each other when they need help dealing with their own fear, anxiety, or anger. IMPORTANT NOTE - THIS IS NOT A THERAPY OR SUPPORT GROUP. Instead, this is a select group of very successful and accomplished women who have a shared experience and while each is navigating their own path, they have an opportunity to learn important information, in a safe place, where they can share their experience, strength, and hope with each other.

I want the invitation/brochure to feel very bespoke, thoughtfully curated, and specifically designed to address the most important and impactful areas of life, health, and wellness. I want the invitation/brochure to communicate that the presenters are the best in class and thought leaders in their respective areas of expertise. I also want to communicate that they have so much to be excited about. Because they have substantial financial resources, they have a unique opportunity to reinvent themselves and lead a life beyond their wildest dreams. I hope they can see how and why they can stop feeling the negative feelings of anger, sadness, fear, guilt, remorse, and regret. My goal is to get them to look forward (as opposed to backward where the negative emotions come from) so they can be optimistic, excited, happy, joyful, and enthusiastic because they get to be whoever they want; live wherever and however they want. They are not defined nor controlled by their past. They have full control and abundant resources at their disposal to be happier and more fulfilled than they ever hoped or imagined.

The feelings of optimism, excitement, energetic, and joyfulness are very important to the messaging of the Open Horizon Circle. I'd like this to be a consistent theme throughout the invitation/brochure. Basically moving from a dark, sad, and negative past to a bright, fun, optimistic, rewarding, fulfilling, and dynamic future.

To create an exciting, rewarding and vibrant life they will want to (in some cases need to) learn new information and skills from the leading authorities in the most important and impactful areas of life.

The presenters at each dinner will focus on one of the "8 Dimensions of Wellness" so they can make thoughtful and informed decisions without fear, anxiety, and stress.

If you think of marriage as two people sailing a ship or flying a plane, the husband and wife often divide the responsibilities of running their affairs because it's too much for one person to manage all by themselves; besides they have a spouse who can help and often times they have different expertise. For illustration purposes, let's say the husband manages the even-numbered items and the wife manages the odd number of items. Each manages half but together everything is well managed and nothing falls through the cracks.

Post-divorce, the husband and wife now each have their own boat to sail and are responsible for all the items (odd and even-numbered) of their ship.

Unfortunately, these women are having to manage items that she has little to no experience with the even-numbered items the husband used to manage during the marriage. They have to take sole control of complicated matters that have serious and long-lasting consequences. That's great if they do a good job. However, given the scope, scale, and complexity of 7-10 figure net worth chances are they won't have the experience, expertise, intellectual resources, and time to manage all the even and odd numbers optimally.

The format of the Open Horizon Circle events will be an intimate dinner conversation, in a private room, at a 5 star restaurant in Chicago. There will be a thoughtfully curated group of 4-10 women at one round table to facilitate an interesting and informative presentation. It will be specifically curated for them and delivered. There is no cost to attend the event and they are welcome to attend as many as they like. I will be covering all the expenses related to dinner, drinks, valet parking, and the speaker or presenter.

Each monthly dinner will focus on 1 of the 8 Dimensions of Wellness:

1. Physical - Physical Activity, Good Nutrition, Sleep, Preventing Illness & Injury, and Managing Chronic Health Conditions.

2. Emotional - Coping Effectively with life and creating satisfying relationships.

3. Social - Developing a sense of connection, belonging, and a well-developed support system.

4. Intellectual - Recognizing one’s creative abilities and finding ways to expand knowledge and skills. Boost cognitive function, stimulate the brain, and fuel learning.

5. Environmental - Occupying pleasant, stimulating environments that support well-being.

6. Spiritual - Expanding a sense of purpose and meaning in life, including one’s morals and ethics. (May or may not involve religious activities). Meditation

7. Vocational - Gaining personal satisfaction and enrichment from one's work (maybe academic or professional). Share your talents, wisdom, and experience.

8. Financial - Satisfaction with current and future financial situations.

I'd like the invitation/brochure to give a general overview of the 8 dimensions of wellness and that each gathering will focus on one of the eight. The presentation will be done by women (some of whom went through a divorce or the death of a spouse) who are widely recognized as experts in their respective fields. The female presenters will be highly qualified and credentialed in their field - this could mean they are MDs or PhDs and/or have decades of experience in their specific area of expertise.

I'd like the invitation to be "timeless" meaning that it doesn't have specific dates, times, or locations included. However, if someone would like more information and details they can call or email me for the specific details of the next couple of dates, topics, locations, and menus. I am also open to having a QR code available on the brochure for them to contact me for additional information. Once they contact my office they will receive I will receive all the detailed information via a PDF so they can RSVP if they would like to attend. My goal is that I don't want the invitation/brochure to expire even though the event details change every month.

I will market the Open Horizon Circle program by distributing the invitation/brochures available via therapists, divorce lawyers, and grief counselors that specialize in this demographic of women in transition. They in turn will share the invitation/brochure with their woman in transition clients if they think they would benefit from the program

The look and feel I am going for with the brochure/invitation is high-end, contemporary, carefully curated content for a very special and specific community of high-net-worth women in transition that has the resources to be and do anything they want.

Vellora
Marlowe Crest
Duvaine
Kestrel Onyx Card
Shopping in Paris and London
Flying private
Vacationing in the Riviera & Monaco.
Beautiful people
Multi-generational - kids and grandkids.

The theme, feel, and messaging of the invitation/brochure should be consistent with the concept of moving away from – sadness, fear, regret, failure, and negative. And moving towards – joyful, happy, optimistic, exciting, successful, energetic, and contentment.

This information is intended to be informative, empowering, uplifting, transformational, and helpful - so they can lead a life that is bigger, brighter, and better than they ever dreamed of experiencing.

Target Market(s)

Wealthy woman who are currently getting divorced, recently divorced, or widowed. Generally the women will be mid-fourties and older..

Industry/Entity Type

Financial Services targeting wealthy windows and divorced woman.

Font styles to use
Serif
Sans Serif

Requirements
Must have
• The look and feel I am going for with the brochure/invitation is high-end, contemporary, carefully curated content for a very special and specific community of high-net-worth women in transition that has the resources to be and do anything they want. PLEASE ENSURE 70% OF THE WOMAN IN THE INVITATAION/BROCHURE OF NON-WHITE RACES & ETHNICITIES. The theme, feel, and messaging of the invitation/brochure should be consistent with the concept of moving away from – sadness, fear, regret, failure, and negative. And moving towards – joyful, happy, optimistic, exciting, successful, energetic, and contentment. This information is intended to be informative, empowering, uplifting, transformational, and helpful - so they can lead a life that is bigger, brighter, and better than they ever dreamed of experiencing.

```html
<!DOCTYPE html>
<html lang="en">
<head>
<meta charset="utf-8">
<title>Open Horizon Circle – Invitation Brochure</title>
<link rel="stylesheet" href="https://fonts.googleapis.com/css2?family=Alfa+Slab+One&family=Montserrat:wght@400;500;600;700&display=swap">
<style>
  :root{
    --stage:#ebebeb;
    --pink-pale:#fbe3ee;
    --pink-soft:#f5c3d9;
    --pink-band:#e36aa5;
    --pink-strip:#eb86b9;
    --pink-line:#e889b6;
    --gold-light:#fbe27a;
    --gold:#f2bf2c;
    --gold-deep:#d99a12;
    --ink:#3a2530;
    --white:#ffffff;
  }
  *{box-sizing:border-box;margin:0;padding:0}
  html,body{width:1200px;height:865px;overflow:hidden;background:var(--stage)}
  body{position:relative;font-family:'Montserrat',sans-serif;color:var(--ink)}

  .paper{
    background:
      radial-gradient(circle at 85% 8%, rgba(236,120,175,.45) 0 9%, transparent 10%),
      radial-gradient(circle at 12% 40%, rgba(255,255,255,.55) 0 7%, transparent 8%),
      radial-gradient(circle at 90% 55%, rgba(236,130,180,.35) 0 8%, transparent 9%),
      radial-gradient(circle at 20% 92%, rgba(236,120,175,.3) 0 10%, transparent 11%),
      linear-gradient(160deg, var(--pink-pale), var(--pink-soft));
  }

  /* ---------- cover ---------- */
  .cover{position:absolute;width:460px;height:635px;left:40px;top:45px;overflow:hidden}
  .cover .art{position:absolute;left:0;top:0;width:460px;height:635px}
  .cover-title{
    position:absolute;left:0;width:460px;top:322px;text-align:center;
    font-family:'Alfa Slab One',serif;line-height:.95;white-space:nowrap;
    transform:rotate(-3deg);
    filter:drop-shadow(1px 2px 0 rgba(150,60,90,.35));
  }
  .cover-title span{
    display:block;
    background:linear-gradient(180deg,var(--gold-light) 10%,var(--gold) 55%,var(--gold-deep));
    -webkit-background-clip:text;background-clip:text;color:transparent;
  }
  .cover-title .line-1{font-size:70px}
  .cover-title .line-2{font-size:40px}
  .cover-strap{
    position:absolute;left:0;width:460px;top:466px;text-align:center;white-space:nowrap;
    color:var(--white);font-size:9.4px;font-weight:600;letter-spacing:.4px;text-transform:uppercase;
    transform:rotate(-3.2deg);
  }
  .cover-note{
    position:absolute;left:25px;top:505px;width:410px;
    border:1.5px solid var(--gold);padding:9px 12px;
    font-size:9.2px;line-height:1.35;text-align:center;
  }
  .cover-note p+p{margin-top:6px}
  .cover-mini{left:0;top:0;transform:scale(.474);transform-origin:0 0}

  /* ---------- spreads ---------- */
  .spread{position:absolute;left:510px;width:436px}
  .spread-top{top:50px;height:300px}
  .spread-bottom{top:375px;height:280px}
  .page{position:absolute;top:0;bottom:0;width:218px;overflow:hidden}
  .page.left{left:0}
  .page.right{left:218px}

  .copy{position:absolute;left:12px;right:12px;font-size:4.3px;line-height:1.38;text-align:justify}
  .copy p+p{margin-top:4px}

  .think{
    position:absolute;left:14px;right:14px;top:100px;height:160px;
    border:.8px solid var(--pink-line);padding:5px 8px;text-align:center;
  }
  .think h3{font-size:6px;font-weight:700;letter-spacing:.4px;margin-bottom:3px}
  .think ul{list-style:none}
  .think li{font-size:4.8px;font-weight:600;padding:3.2px 0;border-bottom:.7px solid var(--pink-line)}
  .think li::before{
    content:"";display:inline-block;width:3px;height:3px;border-radius:50%;
    background:var(--pink-band);margin-right:3px;vertical-align:middle;
  }
  .think li:last-child{border-bottom:none}

  .dimensions-title{font-size:6.2px;font-weight:700;line-height:1.3;text-transform:uppercase;text-align:left}
  .dimensions{list-style:none;margin:4px 0 5px}
  .dimensions li{font-size:4.3px;line-height:1.3;margin-bottom:2.4px;text-align:left}
  .dimensions strong{display:block;font-size:4.8px}
</style>
</head>
<body>

<!-- front cover -->
<section class="cover paper">
  <svg class="art" viewBox="0 0 460 635">
    <defs>
      <radialGradient id="portraitTone" cx="50%" cy="40%" r="60%">
        <stop offset="0" stop-color="#e9c2a6"/>
        <stop offset=".45" stop-color="#8a5a3c"/>
        <stop offset=".75" stop-color="#c9b9b4"/>
        <stop offset="1" stop-color="#f4f1f2"/>
      </radialGradient>
    </defs>
    <circle cx="230" cy="215" r="198" fill="#ffffff"/>
    <g role="img" aria-label="Portrait photo of a smiling woman">
      <circle cx="230" cy="225" r="168" fill="url(#portraitTone)"/>
    </g>
    <circle cx="230" cy="215" r="202" fill="none" stroke="#f2bf2c" stroke-width="4"/>
    <polygon points="0,352 460,312 460,440 0,470" fill="#e36aa5" opacity=".92"/>
    <polygon points="0,470 460,440 460,466 0,494" fill="#eb86b9"/>
  </svg>
  <h1 class="cover-title"><span class="line-1">OPEN</span><span class="line-2">HORIZON CIRCLE</span></h1>
  <p class="cover-strap">I created this educatonal program because there is an unmet need</p>
  <div class="cover-note">
    <p>I am a financial advisor to a small number of ultra high net worth families and I am also married to one of the most prominent family law attorneys in the country.</p>
    <p>This combination of experience and perspective allowed me to see there is no mechanism to help these wealthy woman as they transition from married (chapter 1) to single (chapter 2) and their circumstances are unique given the complexity of their financial circumstances.</p>
  </div>
</section>

<!-- inside spread with list -->
<section class="spread spread-top">
  <div class="page left paper">
    <div class="copy" style="top:12px">
      <p>I'd like this invitation to be timeless, so it carries no dates, times or locations. If you would like more information, call or email my office for the details of the next dinners, topics, locations and menus. A QR code is also available so you can reach me easily. Once you contact us you will receive every detail in a PDF so you can RSVP if you would like to attend.</p>
      <p>This invitation is shared by therapists, divorce lawyers and grief counselors who work with women in transition and believe you would benefit from the program.</p>
      <p>The look and feel is high-end and contemporary, with carefully curated content for a very special community that has the resources to be and do anything they want.</p>
    </div>
    <div class="think">
      <h3>THINK :</h3>
      <ul>
        <li>Vellora</li>
        <li>Marlowe Crest</li>
        <li>Duvaine</li>
        <li>Spontaneous Choices</li>
        <li>Shopping in Paris and London</li>
        <li>Flying Private</li>
        <li>Dining in the Riviera</li>
        <li>Beautiful People</li>
        <li>Multi Generational - Kids and Grandkids - Holiday Gatherings</li>
        <li>Happiness, Smiling Laughing and Joyful People</li>
      </ul>
    </div>
    <div class="copy" style="top:266px">
      <p>I am providing a very unique and valuable resource at a very critical time so that every woman can look forward rather than backward, and feel optimistic, excited and joyful about all that lies ahead. She is not defined nor controlled by her past, and has every resource to create the life she wants.</p>
    </div>
  </div>
  <div class="page right">
    <section class="cover cover-mini paper">
      <svg class="art" viewBox="0 0 460 635">
        <defs>
          <radialGradient id="portraitToneMini" cx="50%" cy="40%" r="60%">
            <stop offset="0" stop-color="#e9c2a6"/>
            <stop offset=".45" stop-color="#8a5a3c"/>
            <stop offset=".75" stop-color="#c9b9b4"/>
            <stop offset="1" stop-color="#f4f1f2"/>
          </radialGradient>
        </defs>
        <circle cx="230" cy="215" r="198" fill="#ffffff"/>
        <g role="img" aria-label="Portrait photo of a smiling woman">
          <circle cx="230" cy="225" r="168" fill="url(#portraitToneMini)"/>
        </g>
        <circle cx="230" cy="215" r="202" fill="none" stroke="#f2bf2c" stroke-width="4"/>
        <polygon points="0,352 460,312 460,440 0,470" fill="#e36aa5" opacity=".92"/>
        <polygon points="0,470 460,440 460,466 0,494" fill="#eb86b9"/>
      </svg>
      <h2 class="cover-title"><span class="line-1">OPEN</span><span class="line-2">HORIZON CIRCLE</span></h2>
      <p class="cover-strap">I created this educatonal program because there is an unmet need</p>
      <div class="cover-note">
        <p>I am a financial advisor to a small number of ultra high net worth families and I am also married to one of the most prominent family law attorneys in the country.</p>
        <p>This combination of experience and perspective allowed me to see there is no mechanism to help these wealthy woman as they transition from married (chapter 1) to single (chapter 2) and their circumstances are unique given the complexity of their financial circumstances.</p>
      </div>
    </section>
  </div>
</section>

<!-- inside spread with wellness topics -->
<section class="spread spread-bottom">
  <div class="page left paper">
    <div class="copy" style="top:12px">
      <p>If you think of marriage as two people sailing a ship or flying a plane, the husband and wife often divide the responsibilities of running their affairs because it is too much for one person to manage alone. Besides, each spouse often brings a different expertise. Say the husband manages the even-numbered items and the wife the odd ones. Each manages half, yet together everything is well managed and nothing falls through the cracks.</p>
      <p>Post-divorce, the husband and wife each have their own boat to sail and are responsible for all of the items, odd and even, of their ship.</p>
      <p>Unfortunately, many women now manage items they have little or no experience with, the even-numbered items the husband used to handle during the marriage. They must take sole control of complicated matters with serious and long-lasting consequences. Given the scope, scale and complexity of a 7-10 figure net worth, few have the experience, expertise and time to manage everything optimally.</p>
      <p>Typically, these women tend to look backward, where feelings of shame, fear, anger and regret are most intense. It is hard to work through these emotions alone, and friends are often not trained, may be married, and rarely have the time to be there when they are needed most.</p>
      <p>Yet I have seen women go on to lead remarkably impressive lives, lives that are fuller, richer, more fun, dynamic and rewarding than they ever expected possible.</p>
      <p>The format of Open Horizon Circle is an intimate dinner conversation in a private room at a five star restaurant in Chicago. A thoughtfully curated group of 4-10 women gathers at one round table for an interesting and informative presentation. There is no cost to attend, and all expenses for dinner, drinks, valet parking and the presenter are covered.</p>
    </div>
  </div>
  <div class="page right paper">
    <div class="copy" style="top:12px">
      <h3 class="dimensions-title">The primary topics that will be discussed are the<br>8 dimensions of wellness</h3>
      <ol class="dimensions">
        <li><strong>1. Physical</strong>Physical Activity, Good Nutrition, Sleep, Preventing Illness &amp; Injury, and Managing Chronic Health Conditions.</li>
        <li><strong>2. Emotional</strong>Coping effectively with life and creating satisfying relationships.</li>
        <li><strong>3. Social</strong>Developing a sense of connection, belonging, and a well-developed support system.</li>
        <li><strong>4. Intellectual</strong>Recognizing one's creative abilities and finding ways to expand knowledge and skills.</li>
        <li><strong>5. Environmental</strong>Occupying pleasant, stimulating environments that support well-being.</li>
        <li><strong>6. Spiritual</strong>Expanding a sense of purpose and meaning in life, including one's morals and ethics. Meditation.</li>
        <li><strong>7. Vocational</strong>Gaining personal satisfaction and enrichment from one's work. Share your talents, wisdom and experience.</li>
        <li><strong>8. Financial</strong>Satisfaction with current and future financial situations.</li>
      </ol>
      <p>Each dinner gives a general overview of the 8 dimensions of wellness and focuses on one of them. Presentations are given by women who are widely recognized as experts in their respective fields, many holding MDs or PhDs, or decades of experience.</p>
      <p>This is not a therapy or support group. It is a select group of very successful and accomplished women with a shared experience, who learn important information in a safe place and share their experience, strength and hope with each other.</p>
      <p>My goal is for every woman to look forward with optimism, excitement and joy, because she gets to be whoever she wants and live wherever and however she wants, bigger, brighter and better than she ever dreamed.</p>
    </div>
  </div>
</section>

</body>
</html>
```